Modern and Elegant business card

A clean and modern but traditional business card is required to reflect the updated LOGO and the new website www.brivexalta.com

The old card as provided is a bit disjointed, crowded and not clear to read especially the company name which is almost hidden in the logo.

The card should take it's queues from the colours of the logo which are green, yellow and orange, bold but rich, not faded or washed out.

We are looking to drastically clean up and improve our old cards

Target Market(s)

Professional Consulting and Business/Government

Industry/Entity Type

Management Consulting

Contact Information for Business Card

The card needs to outlined the new Service Groups as seen on the new site: http://brivexalta.com/services/ New logo needs to be included
The usual info for phones, address and name and email

Font styles to use
Serif
Sans Serif

Colors
fbee3d
f78f20
9bcb3c

Requirements
Must have
• New logo as seen on the current site and provided here
• Service Groups as seen http://brivexalta.com/services/
• Needs to be functional and clean, well proportioned and organized
Nice to have
• Name of cities where offices are located

```html
<!DOCTYPE html>
<html lang="en">
<head>
<meta charset="utf-8">
<title>Brivexalta business card</title>
<link rel="stylesheet" href="https://fonts.googleapis.com/css2?family=Crimson+Text:wght@400;600;700&display=swap">
<style>
  :root {
    --stage: #1f1f1f;
    --paper: #ffffff;
    --ink: #1d1d1d;
    --band: #262525;
    --band-light: #f2f2f2;
    --sun-yellow: #fbee3d;
    --sun-orange: #f78f20;
    --accent-red: #e8452a;
    --leaf-green: #9bcb3c;
  }
  * { margin: 0; padding: 0; box-sizing: border-box; }
  html, body { width: 1200px; height: 660px; overflow: hidden; }
  body {
    background: var(--stage);
    font-family: "Crimson Text", Georgia, serif;
    color: var(--ink);
    position: relative;
  }
  .card {
    position: absolute;
    width: 520px;
    height: 297px;
    background: var(--paper);
    overflow: hidden;
    box-shadow: 0 12px 30px rgba(0,0,0,.55);
  }
  .card--services { left: 50px; top: 120px; }
  .card--contact { left: 630px; top: 243px; }
  .card__art { position: absolute; inset: 0; width: 100%; height: 100%; }

  .wordmark {
    position: absolute;
    display: flex;
    align-items: center;
    gap: 10px;
    font-weight: 700;
    text-transform: uppercase;
    letter-spacing: 2px;
    color: var(--ink);
    line-height: 1;
  }
  .wordmark__dot {
    width: 18px; height: 18px; border-radius: 50%;
    background: var(--sun-orange);
  }
  .card--services .wordmark { left: 40px; top: 130px; font-size: 34px; }
  .card--contact .wordmark { right: 30px; top: 60px; font-size: 28px; }

  .services {
    position: absolute;
    left: 300px; top: 52px;
    width: 200px;
    list-style: none;
    text-align: center;
    font-size: 14px;
    line-height: 16px;
    color: var(--ink);
  }

  .person { position: absolute; left: 30px; top: 118px; }
  .person__name { font-size: 17px; font-weight: 700; letter-spacing: 1px; text-transform: uppercase; }
  .person__role { font-size: 14px; line-height: 15px; }
  .person__role--partner { color: var(--accent-red); }
  .person__role--office { color: var(--sun-orange); }

  .contact {
    position: absolute;
    list-style: none;
    color: var(--band-light);
    font-size: 14px;
    line-height: 17px;
  }
  .contact li { display: flex; align-items: flex-start; gap: 7px; }
  .contact svg { width: 12px; height: 12px; margin-top: 3px; flex: none; }
  .contact--direct { left: 28px; bottom: 14px; }
  .contact--office { right: 28px; top: 164px; }
</style>
</head>
<body>

  <section class="card card--services">
    <svg class="card__art" viewBox="0 0 520 297" aria-hidden="true">
      <defs>
        <linearGradient id="arcWarm" x1="0" y1="0" x2="0" y2="1">
          <stop offset="0" stop-color="#e8452a"/>
          <stop offset="0.5" stop-color="#fbee3d"/>
          <stop offset="1" stop-color="#f78f20"/>
        </linearGradient>
      </defs>
      <path d="M230 20 Q330 160 240 290" fill="none" stroke="url(#arcWarm)" stroke-width="2.5"/>
      <path d="M490 10 Q540 150 500 290" fill="none" stroke="url(#arcWarm)" stroke-width="2"/>
    </svg>
    <div class="wordmark"><span class="wordmark__dot"></span>Brivexalta</div>
    <ul class="services">
      <li>Export Market Development</li>
      <li>Business Strategy</li>
      <li>Energy Sector Strategy</li>
      <li>Community And</li>
      <li>Economic Development</li>
      <li>Commercial/Retail Business</li>
      <li>Optimization Strategy</li>
      <li>Strategic Communications</li>
      <li>Branding and Social Media</li>
    </ul>
  </section>

  <section class="card card--contact">
    <svg class="card__art" viewBox="0 0 520 297" aria-hidden="true">
      <defs>
        <linearGradient id="sweepWarm" x1="0" y1="0" x2="1" y2="0">
          <stop offset="0" stop-color="#e8452a"/>
          <stop offset="0.45" stop-color="#fbee3d"/>
          <stop offset="1" stop-color="#f78f20"/>
        </linearGradient>
      </defs>
      <path class="band" d="M0 235 Q260 150 520 112 L520 297 L0 297 Z" fill="#262525"/>
      <path d="M0 226 Q260 142 520 104" fill="none" stroke="url(#sweepWarm)" stroke-width="4"/>
    </svg>

    <div class="wordmark"><span class="wordmark__dot"></span>Brivexalta</div>

    <div class="person">
      <p class="person__name">Mara Lindqvist</p>
      <p class="person__role person__role--partner">Senior Partner, Western Canada</p>
      <p class="person__role person__role--office">Chief Operating Officer</p>
    </div>

    <ul class="contact contact--office">
      <li>
        <svg viewBox="0 0 12 12"><circle cx="6" cy="6" r="5" fill="none" stroke="#f78f20" stroke-width="1.3"/><path d="M1 6h10M6 1c-3 3-3 7 0 10M6 1c3 3 3 7 0 10" fill="none" stroke="#f78f20" stroke-width="1"/></svg>
        <span>www.brivexalta.com</span>
      </li>
      <li>
        <svg viewBox="0 0 12 12"><path d="M6 11.5C3 8 2 6.3 2 4.5a4 4 0 0 1 8 0c0 1.8-1 3.5-4 7z" fill="#f78f20"/><circle cx="6" cy="4.5" r="1.5" fill="#262525"/></svg>
        <span>4120 - 88 Avenue NW<br>Edmonton AB Canada T6B 2R7</span>
      </li>
    </ul>

    <ul class="contact contact--direct">
      <li>
        <svg viewBox="0 0 12 12"><rect x="3" y="0.5" width="6" height="11" rx="1" fill="none" stroke="#fbee3d" stroke-width="1.3"/><circle cx="6" cy="9.5" r=".8" fill="#fbee3d"/></svg>
        <span>(780) 555-0142</span>
      </li>
      <li>
        <svg viewBox="0 0 12 12"><path d="M2 1.5l2.2-.5 1.3 2.8-1.3 1c.7 1.5 1.6 2.4 3 3l1-1.3 2.8 1.3-.5 2.2C5.5 10.5 1.5 6.5 2 1.5z" fill="#f78f20"/></svg>
        <span>(780) 555-0187</span>
      </li>
      <li>
        <svg viewBox="0 0 12 12"><rect x="0.5" y="2" width="11" height="8" fill="#f78f20"/><path d="M0.5 2l5.5 4.5L11.5 2" fill="none" stroke="#262525" stroke-width="1"/></svg>
        <span>mara@brivexalta.com</span>
      </li>
    </ul>
  </section>

</body>
</html>
```